Bottled Margarita Label Project

We need a label design (using a 750 ml bottle) for an all natural, premium, Ready to Drink (as in pre-mixed) Margarita. The brand is called VONDRA Pure Margarita. We were tired of the chemical, sugary, preservative laden "margaritas" with artificial colorings and cheap tequilas, so we developed a simple, straightforward CLASSIC, ingredient driven margarita made with only the purest, traditional ingredients: 100% Blue Agave Tequila Reposado, Double Distilled Orange Liqueur, Lime Juice and sweetened with Organic Cane Sugar. The result is a pure margarita, the kind you got on that amazing beach vacation in Mexico. This is a product that can be chilled and served over ice or straight up. You might grab one to take to a BBQ or to the beach. It's simple, sexy and classic. We are hoping the final design can communicate purity, integrity of ingredients and the freedom one might feel when on vacation in the sun. This doesnt have to be a Latin themed beverage, but more of a Summer / chill / "sala del oro" in a bottle vibe. Thank you!

Target Market(s)

25 to 45 year olds who feel they know what makes up a good margarita. Aspirational types who love adventurous vacations but are not necessarily wealthy. Our customer doesn't always have the time to make a real margarita from scratch but wish they could get a decent one in a bottle that doesn't taste artificial. They are brand and label conscious and will pay a little more for quality as long as there is value.

Industry/Entity Type

Cafe

Requirements
Must have
• Must have "Vondra" and "pure margartia" clearly listed as the name of the beverage. Must also make clear that this is "Premium", "Ready to Drink" and "Made with 100% Blue Agave Tequila"
Nice to have
• We really love designs that are clean and uncluttered. We have imagined a clear 750ml bottle. Think about tequila when you think about this label. This is a hand made, artisan product produced in batches. We are looking for a finished label/bottle that is colorful, transcendent, artisinal and timeless. It should be mature but not stuffy. It should be simple and sexy - not splashy, brash or silly. Our competition is Tidy Moth Margarita, Rafa Tolentes, and Brevo pre-mixed margaritas which are fake margaritas made in huge factories. Vondra is made with integrity and honest ingredients. For colors, greens come to mind but we are totally open to a designer's vision ;). This should be a product that a fashion forward airline like Halcyon Skyways would want serve and a bottle that a savvy drinker would choose over the bland, mainstream brands. Check out Munrez Cachaça for a sexy, vibrant take on a bottle of alcohol with a Summer slant. Also look at Velquiro tequila. They have a wonderful label that blends vintage and modern elements with minimalist design and comes off as handmade.
Should not have
• Elements we do NOTwant to see any red colors, sombreros, parrots, tiki masks, palm trees, spring break, deserted islands, or Dale Hornsby imagery. This should be a product that an airline like Halcyon Skyways would want to serve.

```html
<!DOCTYPE html>
<html lang="en">
<head>
<meta charset="utf-8">
<title>VONDRA Pure Margarita – Bottle Label</title>
<link href="https://fonts.googleapis.com/css2?family=Alegreya&family=Cinzel:wght@500&family=Fondamento&display=swap" rel="stylesheet">
<style>
  :root {
    --page: #ffffff;
    --paper-light: #eef2c8;
    --paper-mid: #a8e0d6;
    --paper-deep: #2fb9cc;
    --brand-green: #1db08c;
    --ink: #3f3f3f;
    --rule: #4a5a58;
    --lime-core: #8cc63f;
    --lime-edge: #3f8f1f;
  }
  html, body {
    margin: 0;
    padding: 0;
    width: 940px;
    height: 1200px;
    overflow: hidden;
    background: var(--page);
  }
  .canvas {
    position: relative;
    width: 940px;
    height: 1200px;
  }
  .label {
    position: absolute;
    left: 115px;
    top: 95px;
    width: 723px;
    height: 1013px;
    overflow: hidden;
    background: linear-gradient(150deg, var(--paper-light) 0%, var(--paper-mid) 45%, var(--paper-deep) 100%);
  }
  .claims {
    position: absolute;
    left: 0;
    top: 52px;
    margin: 0;
    padding: 0;
    list-style: none;
    font-family: "Fondamento", cursive;
    font-size: 21px;
    color: var(--ink);
    letter-spacing: 0.5px;
  }
  .claims li {
    width: 350px;
    padding: 0 0 4px 20px;
    border-bottom: 1px solid var(--rule);
    margin-bottom: 9px;
    line-height: 32px;
    white-space: nowrap;
  }
  .claims li:last-child { width: 330px; }
  .product-name {
    position: absolute;
    left: 203px;
    top: 540px;
    margin: 0;
    font-family: "Alegreya", serif;
    font-weight: 400;
    font-size: 76px;
    line-height: 66px;
    color: var(--ink);
  }
  .brand {
    position: absolute;
    left: 490px;
    top: 20px;
    width: 200px;
    height: 930px;
  }
  .brand text {
    font-family: "Cinzel", serif;
    font-weight: 500;
    fill: var(--brand-green);
  }
  .lime {
    position: absolute;
    left: 5px;
    top: 895px;
    width: 240px;
    height: 240px;
    border-radius: 50%;
    background: radial-gradient(circle, var(--lime-core) 0%, #6fb233 70%, var(--lime-edge) 100%);
  }
  .volume {
    position: absolute;
    left: 295px;
    top: 968px;
    margin: 0;
    font-family: "Alegreya", serif;
    font-size: 24px;
    color: var(--ink);
    word-spacing: 4px;
  }
</style>
</head>
<body>
<div class="canvas">
  <div class="label">
    <ul class="claims">
      <li>ready to drink</li>
      <li>premium ingredients</li>
      <li>made with 100% blue agave tequila</li>
    </ul>

    <h1 class="product-name">pure<br>margarita</h1>

    <svg class="brand" viewBox="0 0 200 930" aria-label="VONDRA">
      <text transform="translate(178 925) rotate(-90)" font-size="225" textLength="920" lengthAdjust="spacingAndGlyphs">VONDRA</text>
    </svg>

    <div class="lime" role="img" aria-label="Photo of a fresh lime slice"></div>

    <p class="volume">45% alc. 750 ml</p>
  </div>
</div>
</body>
</html>
```